Healthcare Technology Company Business Card Design

Hi,

We require a new business card design thats catchy and professional.
Our target audience is healthcare professionals. See supplied artwork for our logo.

If you think its achievable please try add the tag line, not necessary however.
"Developing technologies to improve patient care and release operation benefits"

We'll require the following information on the card. No need to have the subject titles but i've referenced them for your convenience.

Personal Details
Paul Dwyer
Position: Director
Phone Number - 03 9472 5836
Mobile Number - 0438 275 904
Email: firstname.lastname@mediqbay.com.au

Company Details
Suite 31, 286 Keldon Street
Westhaven, Victoria
Fax: 03 8241 3975
mediqbay.com.au

Prefer a thinner design than the normal stock standard business card dimensions.
Please ensure there is adequate bleed.

Target Market(s)

Healthcare Professionals

Industry/Entity Type

Healthcare

Font styles to use
Sans Serif

Requirements
Must have
• Clean, Sharp Looks
Should not have
• Any healthcare symbols

```html
<!DOCTYPE html>
<html lang="en">
<head>
<meta charset="utf-8">
<title>Mediqbay Business Card</title>
<link rel="stylesheet" href="https://fonts.googleapis.com/css2?family=Open+Sans:wght@400;600;700&display=swap">
<style>
  :root {
    --bg: #e9e9ee;
    --card: #ffffff;
    --navy: #2f6690;
    --orange: #f0932b;
    --ink: #3a3a3a;
    --rule: #b9b9b9;
  }
  * { box-sizing: border-box; margin: 0; padding: 0; }
  html, body {
    width: 1200px; height: 987px; overflow: hidden;
    background: var(--bg);
    font-family: "Open Sans", Arial, sans-serif;
    color: var(--ink);
  }
  .card {
    position: absolute;
    left: 200px;
    width: 800px; height: 420px;
    background: var(--card);
    border-radius: 34px;
    box-shadow: 0 2px 10px rgba(0,0,0,0.12);
    overflow: hidden;
  }
  .card--back { top: 52px; }
  .card--front { top: 515px; }

  /* back */
  .back-brand {
    position: absolute; left: 0; right: 0; top: 130px;
    text-align: center;
    font-size: 112px; font-weight: 700; letter-spacing: -3px;
    color: var(--navy); line-height: 1;
  }
  .back-web {
    position: absolute; left: 0; right: 0; top: 290px;
    text-align: center;
    font-size: 24px; letter-spacing: 7px; color: var(--ink);
  }

  /* front */
  .front-brand {
    position: absolute; left: 60px; top: 50px;
    display: flex; align-items: center; gap: 18px;
  }
  .front-brand__dot {
    width: 56px; height: 56px; background: var(--orange);
  }
  .front-brand__name {
    font-size: 76px; font-weight: 700; letter-spacing: -2px;
    color: var(--navy); line-height: 1;
  }
  .divider {
    position: absolute; left: 0; right: 0; top: 206px; height: 3px;
    background: linear-gradient(90deg, rgba(185,185,185,0) 0%, var(--rule) 40%, #999 100%);
  }
  .person {
    position: absolute; right: 50px; top: 160px;
    font-size: 30px; line-height: 1;
  }
  .person__name { color: var(--orange); font-weight: 700; }
  .person__role { color: var(--navy); font-weight: 400; font-size: 26px; }

  .contacts {
    position: absolute; left: 54px; top: 236px;
    list-style: none;
    font-size: 21px; line-height: 30px;
  }
  .contacts li { display: flex; align-items: center; gap: 10px; }
  .contacts svg { width: 16px; height: 16px; flex: none; }

  .address {
    position: absolute; right: 50px; bottom: 40px;
    text-align: right;
    font-size: 23px; line-height: 32px;
    font-style: normal;
  }
</style>
</head>
<body>

<section class="card card--back" aria-label="Card back">
  <div class="back-brand">mediqbay</div>
  <div class="back-web">www.mediqbay.com.au</div>
</section>

<section class="card card--front" aria-label="Card front">
  <div class="front-brand">
    <span class="front-brand__dot"></span>
    <span class="front-brand__name">mediqbay</span>
  </div>

  <div class="person">
    <span class="person__name">Paul Dwyer,</span>
    <span class="person__role">Director</span>
  </div>

  <div class="divider"></div>

  <ul class="contacts">
    <li>
      <svg viewBox="0 0 16 16" aria-hidden="true"><circle cx="8" cy="8" r="7" fill="none" stroke="#f0932b" stroke-width="1.6"/><path d="M5.5 4.5c0 4 2 6 6 6l-1.2-1.8-1.4.6-2.2-2.2.6-1.4z" fill="#f0932b"/></svg>
      03 9472 5836
    </li>
    <li>
      <svg viewBox="0 0 16 16" aria-hidden="true"><rect x="4.5" y="1.5" width="7" height="13" rx="1.5" fill="none" stroke="#f0932b" stroke-width="1.6"/><circle cx="8" cy="12" r="0.9" fill="#f0932b"/></svg>
      0438 275 904
    </li>
    <li>
      <svg viewBox="0 0 16 16" aria-hidden="true"><rect x="4" y="1.5" width="8" height="5" fill="none" stroke="#f0932b" stroke-width="1.4"/><rect x="1.5" y="6.5" width="13" height="7" rx="1.5" fill="#f0932b"/></svg>
      03 8241 3975
    </li>
    <li>
      <svg viewBox="0 0 16 16" aria-hidden="true"><rect x="1.5" y="3.5" width="13" height="9" rx="1" fill="#f0932b"/><path d="M2 4l6 5 6-5" fill="none" stroke="#fff" stroke-width="1.3"/></svg>
      firstname.lastname@mediqbay.com.au
    </li>
    <li>
      <svg viewBox="0 0 16 16" aria-hidden="true"><circle cx="8" cy="8" r="6.5" fill="#f0932b"/><path d="M1.5 8h13M8 1.5c-3 3.5-3 9.5 0 13M8 1.5c3 3.5 3 9.5 0 13" fill="none" stroke="#fff" stroke-width="1"/></svg>
      www.mediqbay.com.au
    </li>
  </ul>

  <address class="address">
    Suite 31<br>
    286 Keldon Street<br>
    Westhaven, Victoria
  </address>
</section>

</body>
</html>
```